B2B EDM Banner Design- Specialist Tech Company

We need a new top-of-email banner for our EDM campaigns for Varnel Brix (www.varnelbrix-example.com
). This banner will sit at the top of every email and must immediately signal the brand, look modern and professional, and be visually aligned with the tech/IT audience.
Size of the banner: Around 728x90 - it must fit at the top of an email blast.
Purpose of the Banner
Establish a strong, recognizable brand identity across all Varnel Brix EDMs
visually consistent with existing banners created for other brands (see reference examples provided)
Communicate Varnel Brix’s value proposition at a glance
Brand Name
Varnel Brix
Tagline (must appear in the banner)
“11,322 whitepapers from 726 companies”
Design Requirements
Style & Tone
Modern, clean, and professional
Tech-centric look and feel
High-quality, sleek, and corporate
Eye-catching but not cluttered
Should feel premium and authoritative
Layout & Composition
Full-width banner for email header
Horizontal orientation similar to the Plomtar and Quindle Staff Archive examples
Include space for the brand name/logo prominently on the left or centered
Integrate the tagline in a readable, secondary position
Optional: a subtle background texture or tech-related abstract pattern (circuitry, network nodes, gradient, etc.)
No busy imagery—should feel clean and trustworthy
Color Palette
Use colors consistent with Varnel Brix branding from www.varnelbrix-example.com
Blues, greys, blacks, and tech-style gradients preferred
Should feel consistent with a B2B IT audience
Typography
Clean, sans-serif fonts (professional/tech-aligned)
Brand name should be bold and prominent
Tagline should be smaller, but still readable on desktop and mobile
Imagery (if used)
Abstract tech shapes, network visuals, geometric patterns, or gradient overlays
Avoid photography of people
Keep imagery subtle so text remains legible
Call-to-Action Button (optional)
None required in this banner (unlike the HR examples)
Banner should remain a pure brand header
Deliverables
Final banner in PNG and JPG formats
2–3 design variations (if possible) for A/B testing
Dimensions optimized for EDM: ~600–700px wide (standard email width), proportionate height

```html
<!DOCTYPE html>
<html lang="en">
<head>
<meta charset="utf-8">
<title>Varnel Brix – EDM Header Banner</title>
<link rel="stylesheet" href="https://fonts.googleapis.com/css2?family=Montserrat:wght@600;800&family=Roboto:wght@400;700;900&display=swap">
<style>
  :root {
    --page-bg: #e3e3e3;
    --banner-light: #1a6f9f;
    --banner-mid: #0f3563;
    --banner-dark: #0c2146;
    --accent: #1ba2e2;
    --white: #ffffff;
    --network-glow: #2aa6e0;
    --map-tone: #1b4f82;
  }
  * { margin: 0; padding: 0; box-sizing: border-box; }
  html, body {
    width: 1200px;
    height: 630px;
    overflow: hidden;
    background: var(--page-bg);
  }
  .banner {
    position: absolute;
    left: 0;
    top: 241px;
    width: 1200px;
    height: 148px;
    background:
      radial-gradient(ellipse 340px 150px at 60px 74px, rgba(32,140,200,0.55), transparent 70%),
      linear-gradient(90deg, var(--banner-light) 0%, var(--banner-mid) 30%, var(--banner-dark) 60%, var(--banner-dark) 100%);
    overflow: hidden;
  }
  .network-decor {
    position: absolute;
    left: 0;
    top: 0;
    width: 148px;
    height: 148px;
    background: radial-gradient(circle at 40% 50%, rgba(42,166,224,0.55) 0%, rgba(42,166,224,0.25) 55%, transparent 75%);
  }
  .world-map {
    position: absolute;
    left: 966px;
    top: 36px;
    width: 190px;
    height: 88px;
    border-radius: 40px;
    background: radial-gradient(ellipse at center, rgba(27,79,130,0.85) 0%, rgba(27,79,130,0.4) 60%, transparent 85%);
  }
  .brand {
    position: absolute;
    left: 304px;
    top: 43px;
    display: flex;
    align-items: center;
  }
  .brand-mark {
    width: 64px;
    height: 64px;
    border-radius: 50%;
    background: var(--accent);
    margin-right: 17px;
  }
  .brand-name {
    font-family: "Montserrat", sans-serif;
    font-weight: 800;
    font-size: 31px;
    line-height: 1;
    color: var(--white);
    letter-spacing: 0.5px;
  }
  .brand-tagline {
    margin-top: 9px;
    font-family: "Montserrat", sans-serif;
    font-weight: 800;
    font-size: 9.5px;
    letter-spacing: 6.4px;
    color: var(--white);
    white-space: nowrap;
  }
  .divider {
    position: absolute;
    left: 641px;
    top: 45px;
    width: 2px;
    height: 59px;
    background: var(--white);
  }
  .stat {
    position: absolute;
    top: 44px;
    text-align: center;
  }
  .stat-figure {
    font-family: "Roboto", sans-serif;
    font-weight: 900;
    font-size: 44px;
    line-height: 1;
    color: var(--accent);
    letter-spacing: 0.5px;
  }
  .stat-label {
    margin-top: 2px;
    font-family: "Roboto", sans-serif;
    font-weight: 400;
    font-size: 15px;
    color: var(--white);
    white-space: nowrap;
  }
  .stat-whitepapers { left: 666px; width: 126px; }
  .stat-companies { left: 818px; width: 78px; }
</style>
</head>
<body>
  <header class="banner">
    <div class="network-decor" role="img" aria-label="Glowing network-node sphere of connected blue points"></div>

    <div class="brand">
      <div class="brand-mark"></div>
      <div class="brand-text">
        <div class="brand-name">VARNEL BRIX</div>
        <div class="brand-tagline">FOR IT PROFESSIONALS</div>
      </div>
    </div>

    <div class="divider"></div>

    <div class="stat stat-whitepapers">
      <div class="stat-figure">11322</div>
      <div class="stat-label">Whitepapers from</div>
    </div>
    <div class="stat stat-companies">
      <div class="stat-figure">726</div>
      <div class="stat-label">Companies</div>
    </div>

    <div class="world-map" role="img" aria-label="Faint blue world map silhouette"></div>
  </header>
</body>
</html>
```